Business Card Design - Local Discount Club

Looking for a fun business card for a local discount club. One side should be the logo only and the other should be have :

Name
Title
Phone, Email
Website

```html
<!DOCTYPE html>
<html lang="en">
<head>
<meta charset="UTF-8">
<title>The Harbor Bay Pass – Business Card</title>
<link href="https://fonts.googleapis.com/css2?family=Montserrat:wght@400;600;700;800&display=swap" rel="stylesheet">
<style>
  :root {
    --bg: #2b2b2d;
    --card-dark: #1f1f20;
    --card-light: #ffffff;
    --brand-blue: #3a56b0;
    --brand-sky: #6fcbea;
    --brand-green: #a8d26a;
    --text-light: #e6e6e6;
    --text-muted: #cfcfcf;
  }
  * { margin: 0; padding: 0; box-sizing: border-box; }
  html, body { width: 1200px; height: 900px; overflow: hidden; }
  body {
    background: var(--bg);
    font-family: "Montserrat", sans-serif;
    display: flex;
    flex-direction: column;
    align-items: center;
    justify-content: center;
    gap: 30px;
  }
  .card {
    position: relative;
    width: 700px;
    height: 400px;
    border-radius: 4px;
    overflow: hidden;
    background: var(--card-dark);
    box-shadow: 0 10px 30px rgba(0,0,0,0.45);
  }
  .stripe {
    position: absolute;
    left: 0; right: 0;
    height: 10px;
    display: flex;
  }
  .stripe span { flex: 1; }
  .stripe .blue { background: var(--brand-blue); }
  .stripe .sky { background: var(--brand-sky); }
  .stripe .green { background: var(--brand-green); }

  .brand-name {
    display: flex;
    align-items: center;
    gap: 14px;
    color: var(--brand-blue);
    font-weight: 800;
    text-transform: uppercase;
    letter-spacing: 1px;
    line-height: 1;
  }
  .brand-name .dot {
    width: 16px; height: 16px;
    border-radius: 50%;
    background: var(--brand-blue);
    flex: none;
  }

  /* Logo side */
  .card--logo .brand-name {
    position: absolute;
    left: 0; right: 0;
    top: 140px;
    justify-content: center;
    font-size: 46px;
  }
  .card--logo .website {
    position: absolute;
    left: 70px;
    bottom: 50px;
    color: var(--text-light);
    font-size: 15px;
    letter-spacing: 0.5px;
  }
  .card--logo .stripe { bottom: 0; }

  /* Info side */
  .card--info .top {
    position: absolute;
    left: 0; right: 0; top: 0;
    height: 235px;
    background: var(--card-light);
  }
  .card--info .brand-name {
    position: absolute;
    left: 0; right: 0;
    top: 95px;
    justify-content: center;
    font-size: 40px;
  }
  .card--info .stripe { top: 235px; }
  .card--info .details {
    position: absolute;
    left: 60px; right: 60px;
    top: 245px; bottom: 0;
    display: flex;
    align-items: center;
    justify-content: center;
    gap: 28px;
  }
  .person { text-align: right; }
  .person-name {
    color: var(--brand-blue);
    font-weight: 700;
    font-size: 26px;
  }
  .person-title {
    color: var(--text-muted);
    font-size: 15px;
    margin-top: 6px;
  }
  .divider {
    width: 2px;
    height: 70px;
    background: var(--brand-blue);
  }
  .contact-list { list-style: none; }
  .contact-list li {
    display: flex;
    align-items: center;
    gap: 10px;
    color: var(--text-light);
    font-size: 14px;
    line-height: 24px;
  }
  .contact-list svg { width: 13px; height: 13px; fill: var(--text-muted); flex: none; }
</style>
</head>
<body>

  <section class="card card--logo" aria-label="Card front">
    <div class="brand-name"><span>The Harbor Bay Pass</span><span class="dot"></span></div>
    <p class="website">www.harborbaypass.com</p>
    <div class="stripe"><span class="blue"></span><span class="sky"></span><span class="green"></span></div>
  </section>

  <section class="card card--info" aria-label="Card back">
    <div class="top">
      <div class="brand-name"><span>The Harbor Bay Pass</span><span class="dot"></span></div>
    </div>
    <div class="stripe"><span class="blue"></span><span class="sky"></span><span class="green"></span></div>
    <div class="details">
      <div class="person">
        <p class="person-name">Daniel Reyes</p>
        <p class="person-title">Owner</p>
      </div>
      <div class="divider"></div>
      <ul class="contact-list">
        <li>
          <svg viewBox="0 0 16 16" aria-hidden="true"><path d="M3.6 1.2l2.3 2.6-1.3 1.9c.9 2 2.6 3.7 4.6 4.6l1.9-1.3 2.6 2.3-1.4 2.3C7 13.4 2.6 9 2.4 2.6z"/></svg>
          +49 404 555 0123
        </li>
        <li>
          <svg viewBox="0 0 16 16" aria-hidden="true"><path d="M1 3h14v10H1zM2 4.2v.4l6 4 6-4v-.4z"/></svg>
          info@harborbaypass.com
        </li>
        <li>
          <svg viewBox="0 0 16 16" aria-hidden="true"><circle cx="8" cy="8" r="6.5"/></svg>
          www.harborbaypass.com
        </li>
      </ul>
    </div>
  </section>

</body>
</html>
```